■依頼の目的/概要
ベストセラー作家が送る最新作の表紙を飾りませんか?
Borelo QuillのBWSの電子書籍表紙デザインをお願いします。

■本の内容
*タイトル:
うつむく朝に灯すひと匙の言葉

というタイトルの表紙デザインの発注になります。

■デザイン要望

要望1つ目
作家名は後でお伝えします。作家名もどこかに挿入いただきたいです。よろしくお願いします。
提出の際は ○○著という形でご提出よろしくお願いします。

要望2つ目
ウェルネスバランスコーチ検定資格保持者

とどこかに入れてください。

要望3つ目
累計Borelo 1位〇冠
(現在、59冠までいっています。今後、出版が控えている作品があります。
そのため、その最終冠数を入れて頂きたいです。)

とどこかに入れてください。

また、出来上がったデザインを作家グループの中で投票にかけて、
一番投票得票数の多かったものを表紙デザインとして選ばせていただきたいと考えております。
もしかしたら、その中で、何か修正依頼など来るかもしれませんが、
それも含めて、ご対応していただける方よろしくお願いします。

また、最終、選考後、
累計Borelo 1位〇〇冠   と記載された表紙と、
累計Borelo 1位〇〇冠   と記載されない表紙の
2表紙の納品をよろしくお願いします。他の部分の表紙のデザイン変更は不要です。
(これは、最終選ばれたデザイナーさんのみご対応で大丈夫です。)

お手数をおかけしますが、よろしくお願いします。

1部内容の抜粋を記載します。

データサイズですが、推奨サイズでJPEGファイルでご納品下さい、よろしくお願いします。
(推奨サイズは2560×1600pxです。)
その他何かご不明な点がございましたら、お気軽にご質問下さい。
よろしくお願いいたします。
変更点がでてきました。

累計Borelo 1位〇〇冠→累計Borelo 1位65冠
と決定しました。最終、この数字でご納品ください。

もうすでに提出済みの方に関しましては、当選後のご対応で大丈夫です。
お手数をおかけしますが、ご対応なにとぞよろしくお願いいたします。
皆様、たくさんのご応募まことにありがとうございました。
コンペというとても厳しい条件にも関わらず、挑戦いただいたことに
大変大変感謝しております。
ご提案されましたすべての作品、デザイナー様のご経歴、作成への思い入れ、
すべてを拝見させていただきました。
これから、作家グループへ全体回覧のメールを致します。
作家グループの皆様の投票結果までお待ちください(場合により結果
公表まで1週間から10日ぐらいかかる場合もあると思われます)。
また、この度、いろいろな作品に触れさせていただきましたこと本当に
本当に感謝いたします。
皆さまのご努力、精進そしてそのチャレンジに大変感謝と尊敬を感じております。
ご経歴やデザイナー様の名前などすべて伏せて、作品のみの提示にて
小説家作家グループに提案させていただきたいと思っております。
ただ、今回の表紙に関しましては、どうしても1名しか選べない状況がございますこと
また、総選挙による投票にて決定致しますこと、ご理解何卒よろしくお願い申しあげます。
また、もしも、今回当選に至らないことがありましても、
今後も私自身は作家生活を継続予定ですので、
(今回は作品の表紙に合わないことがあっても)作風の気に入ったデザイナー様には
個人的にお話を相談させていただく場合もあると思っております。
また、別の作品の表紙を飾っていただく可能性もあるかと思っております。
この度は誠に誠にありがとうございました。
表紙ですが、最終選考決定いたしました。
当選された方には個別に連絡をさせていただきました。

皆様からのご提案、そして、そのチャレンジに敬意と感謝をしております。
私はこれからも作家活動を継続致しますので、また、ご一緒にお仕事をさせていただき
表紙を飾っていただく機会もあるかと思います。
その際はなにとぞよろしくお願いもうしあげます。
自分のためだけでなく、ベストセラーを取り続けることで、素晴らしい表紙を飾れるチャンスをこれからも作りたいと思い、また、精進していきたいと思います。
この度はまことにありがとうございました。

「目が惹きつけられました」とか
これから上を向いて、光を見て行こうとする視線と深く、それでいて爽やかなブルーのタッチがとても印象的で綺麗‼️
など目が離せない、というようなコメントを多くいただきました。
ご提出誠にありがとうございます。

コンペについてはとても厳しい条件にも関わらず挑戦していただき、
本当に一つのタイトルに対する皆様の創造力について驚きや才能についてをいつも
感じています。
そして、そのチャレンジする姿勢にいつもエネルギーをいただき、
私自身もこれからも、いろいろなことに挑戦する姿勢を続けていきたいな、
と感じております。
表紙を飾っていただく機会もあるかと思います。
その際はなにとぞよろしくお願いもうしあげます。この度はありがとうございました。

```html
<!DOCTYPE html>
<html lang="ja">
<head>
<meta charset="utf-8">
<title>うつむく朝に灯すひと匙の言葉</title>
<link href="https://fonts.googleapis.com/css2?family=Noto+Sans+JP:wght@700;900&family=Shippori+Mincho:wght@600;800&display=swap" rel="stylesheet">
<style>
  :root {
    --cover-yellow: #f8e23b;
    --sun-orange: #f2a532;
    --band-orange: #f1ad47;
    --ink: #2b2019;
    --paper: #ffffff;
    --badge-dark: #3a2a1e;
    --badge-gold: #e9c873;
    --face-tone: #f6cf9a;
  }
  * { margin: 0; padding: 0; box-sizing: border-box; }
  html, body { width: 750px; height: 1200px; overflow: hidden; background: var(--cover-yellow); }
  .cover {
    position: relative; width: 750px; height: 1200px; overflow: hidden;
    background: var(--cover-yellow);
    font-family: "Noto Sans JP", sans-serif; color: var(--ink);
  }
  .expression-grid {
    position: absolute; left: 38px; top: 38px; width: 424px; height: 262px;
    background: linear-gradient(180deg, #fbe98a, var(--face-tone));
    border-radius: 10px; opacity: .85;
  }
  .sun-circle {
    position: absolute; left: 110px; top: 272px; width: 460px; height: 440px;
    border-radius: 50%; background: var(--sun-orange);
  }
  .title-vertical {
    position: absolute; left: 618px; top: 30px;
    writing-mode: vertical-rl; font-weight: 900; font-size: 82px; line-height: 1;
    letter-spacing: 2px;
  }
  .title-vertical .small { font-size: 62px; }
  .title-lead {
    position: absolute; left: 140px; top: 440px; font-weight: 900; font-size: 66px; line-height: 1;
  }
  .title-ruby {
    position: absolute; left: 352px; top: 300px;
    font-family: "Shippori Mincho", serif; font-weight: 800; font-size: 44px; letter-spacing: 14px;
  }
  .title-key {
    position: absolute; left: 292px; top: 356px; font-weight: 900; font-size: 220px; line-height: 1;
  }
  .title-particle {
    position: absolute; left: 520px; top: 520px; font-weight: 900; font-size: 78px; line-height: 1;
  }
  .helper-figure {
    position: absolute; left: 112px; top: 540px; width: 100px; height: 122px;
    border-radius: 44px 44px 8px 8px;
    background: linear-gradient(180deg, var(--face-tone), #ffffff);
  }
  .word-boxes { position: absolute; left: 212px; top: 645px; display: flex; gap: 22px; }
  .word-box {
    width: 118px; height: 108px; background: var(--paper); border: 5px solid var(--ink);
    display: flex; align-items: center; justify-content: center;
    font-weight: 900; font-size: 80px; line-height: 1;
  }
  .author-band {
    position: absolute; left: 0; top: 968px; width: 750px; height: 214px;
    background: var(--band-orange);
  }
  .credential {
    position: absolute; left: 60px; top: 1000px;
    font-family: "Shippori Mincho", serif; font-weight: 600; font-size: 36px; line-height: 1.38;
    letter-spacing: 1px;
  }
  .author-line {
    position: absolute; left: 60px; top: 1108px; display: flex; align-items: center; gap: 6px;
    font-family: "Shippori Mincho", serif; font-weight: 600; font-size: 34px;
  }
  .author-dot { width: 40px; height: 40px; border-radius: 50%; background: var(--ink); }
  .author-slash { font-size: 48px; margin: 0 2px 0 10px; font-weight: 400; }
  .rank-badge {
    position: absolute; left: 598px; top: 962px; width: 146px; height: 146px;
    border-radius: 50%; background: var(--badge-dark); border: 4px solid var(--badge-gold);
    display: flex; flex-direction: column; align-items: center; justify-content: center;
    color: var(--badge-gold); font-family: "Shippori Mincho", serif; font-weight: 800; text-align: center;
  }
  .rank-badge .line-one { font-size: 19px; line-height: 1.3; }
  .rank-badge .line-two { font-size: 28px; line-height: 1.2; }
</style>
</head>
<body>
<main class="cover">
  <div class="expression-grid" role="img" aria-label="Grid of eight small character illustrations showing different moods"></div>
  <div class="sun-circle"></div>

  <h1 class="title-vertical">うつむく朝<span class="small">に</span>灯す</h1>
  <div class="title-lead">ひと</div>
  <div class="title-ruby">さじ</div>
  <div class="title-key">匙</div>
  <div class="title-particle">の</div>

  <div class="helper-figure" role="img" aria-label="Small illustration of a caring helper figure"></div>

  <div class="word-boxes">
    <div class="word-box">言</div>
    <div class="word-box">葉</div>
  </div>

  <div class="author-band"></div>
  <p class="credential">ウェルネスバランスコーチ<br>検定資格保持者</p>
  <p class="author-line">
    <span class="author-dot"></span><span class="author-dot"></span><span class="author-dot"></span><span class="author-dot"></span><span class="author-dot"></span>
    <span class="author-slash">/</span>著
  </p>

  <div class="rank-badge">
    <span class="line-one">累計Borelo</span>
    <span class="line-two">1位65冠</span>
  </div>
</main>
</body>
</html>
```